Interior Design business card design

I am an interior decorator - dont want to specify decorating more just design.
Want organic looking logo - charcoal and white - with touch of lime green.
Like the idea of some sort of spiral in corner but writing in a line
want lower case, tildamarchetti as one and designs in different font underneath. Maybe using t and m as logo.
More modern than traditional. My clients are mid to top end residential

Target Market(s)

medium to top end homeowners

Industry/Entity Type

Residential

Contact Information for Business Card

Tilda Marchetti Designs
58 Kellaway ave
Pemberly 2190 NSW
Tel 0417268914
tildamarchetti@velnaro.com.au

Logo Text

Tilda Marchetti Designs

Logo styles of interest
Abstract Logo
Lettermark Logo
Requirements
Must have
• Name address ph and e mail
Nice to have
• Contemporary
smart but organic
Should not have
• no traditional fonts

```html
<!DOCTYPE html>
<html lang="en">
<head>
<meta charset="utf-8">
<title>Tilda Marchetti Designs – Business Cards</title>
<link href="https://fonts.googleapis.com/css2?family=Questrial&display=swap" rel="stylesheet">
<style>
  :root {
    --backdrop: #e6e6e3;
    --paper: #fbfbfa;
    --charcoal: #5a5a5f;
    --ink: #55555b;
    --ink-soft: #6a6a70;
    --on-dark: #e9e9ec;
    --mark-light: #d6d6da;
    --lime: #8cc63f;
  }
  * { box-sizing: border-box; margin: 0; padding: 0; }
  html, body {
    width: 1200px; height: 800px; overflow: hidden;
    background: var(--backdrop);
    font-family: "Questrial", "Century Gothic", sans-serif;
  }
  .stage {
    position: relative; width: 1200px; height: 800px;
    display: flex; align-items: center; justify-content: center; gap: 40px;
  }
  .card {
    position: relative; width: 520px; height: 318px;
    box-shadow: 0 6px 18px rgba(0,0,0,.14);
  }
  .card--front { background: var(--paper); color: var(--ink); }
  .card--back { background: var(--charcoal); color: var(--on-dark); }

  .brand-name {
    position: absolute; font-size: 22px; line-height: 1.2; letter-spacing: .2px;
    font-weight: 400; white-space: nowrap;
  }
  .brand-name__line { display: block; }
  .card--front .brand-name { left: 44px; top: 46px; color: var(--ink); }
  .card--back .brand-name { right: 44px; top: 38px; text-align: right; color: var(--on-dark); }

  .brand-square { position: absolute; width: 78px; height: 78px; }
  .card--front .brand-square { right: 52px; top: 46px; background: var(--ink); }
  .card--back .brand-square { left: 60px; top: 56px; background: var(--mark-light); }

  .contact {
    position: absolute; bottom: 30px; font-size: 12.5px; line-height: 1.6;
    font-style: normal;
  }
  .card--front .contact { left: 44px; color: var(--ink-soft); }
  .card--back .contact { right: 40px; text-align: right; color: var(--on-dark); }
  .contact__line { display: flex; align-items: center; gap: 6px; }
  .card--back .contact__line { justify-content: flex-end; }
  .contact__item { display: inline-flex; align-items: center; gap: 5px; margin-right: 10px; }
  .contact__item:last-child { margin-right: 0; }
  .icon { width: 12px; height: 12px; flex: none; }
</style>
</head>
<body>
<main class="stage">
  <section class="card card--front" aria-label="Business card front">
    <p class="brand-name">
      <span class="brand-name__line">tildamarchetti</span>
      <span class="brand-name__line">designs</span>
    </p>
    <span class="brand-square" aria-hidden="true"></span>
    <address class="contact">
      <p class="contact__line">58 Kellaway ave Pemberly 2190 NSW</p>
      <p class="contact__line">
        <span class="contact__item">
          <svg class="icon" viewBox="0 0 12 12" aria-hidden="true"><circle cx="6" cy="6" r="6" fill="var(--lime)"/><path d="M4 3.2l1 1.3-.6.8c.5.9 1.1 1.5 2 2l.8-.6 1.3 1-.5 1C6.3 8.7 3.3 5.7 3.3 3.7z" fill="#fff"/></svg>
          0417268914
        </span>
        <span class="contact__item">
          <svg class="icon" viewBox="0 0 12 12" aria-hidden="true"><circle cx="6" cy="6" r="6" fill="var(--lime)"/><rect x="3" y="4" width="6" height="4.2" rx=".5" fill="#fff"/><path d="M3.2 4.3L6 6.4l2.8-2.1" stroke="var(--lime)" stroke-width=".7" fill="none"/></svg>
          tildamarchetti@velnaro.com.au
        </span>
      </p>
    </address>
  </section>

  <section class="card card--back" aria-label="Business card back">
    <span class="brand-square" aria-hidden="true"></span>
    <p class="brand-name">
      <span class="brand-name__line">tildamarchetti</span>
      <span class="brand-name__line">designs</span>
    </p>
    <address class="contact">
      <p class="contact__line">58 Kellaway ave Pemberly 2190 NSW</p>
      <p class="contact__line">
        <span class="contact__item">
          <svg class="icon" viewBox="0 0 12 12" aria-hidden="true"><circle cx="6" cy="6" r="6" fill="var(--lime)"/><path d="M4 3.2l1 1.3-.6.8c.5.9 1.1 1.5 2 2l.8-.6 1.3 1-.5 1C6.3 8.7 3.3 5.7 3.3 3.7z" fill="#fff"/></svg>
          0417268914
        </span>
        <span class="contact__item">
          <svg class="icon" viewBox="0 0 12 12" aria-hidden="true"><circle cx="6" cy="6" r="6" fill="var(--lime)"/><rect x="3" y="4" width="6" height="4.2" rx=".5" fill="#fff"/><path d="M3.2 4.3L6 6.4l2.8-2.1" stroke="var(--lime)" stroke-width=".7" fill="none"/></svg>
          tildamarchetti@velnaro.com.au
        </span>
      </p>
    </address>
  </section>
</main>
</body>
</html>
```